Medical VIP club - small design

Please read the specs in a design brief attached. Also we don't have logo in a Vector format and attaching the only version we have.

Industry/Entity Type

Club

```html
<!DOCTYPE html>
<html lang="en">
<head>
<meta charset="utf-8">
<title>Veridel — Services</title>
<link rel="stylesheet" href="https://fonts.googleapis.com/css2?family=Arimo&family=Libre+Baskerville&family=Petit+Formal+Script&display=swap">
<style>
  :root {
    --bg-dark: #4a2f1c;
    --bg-mid: #5b3d27;
    --footer: #3d2716;
    --footer-edge: #2c1b0e;
    --panel: #8a7550;
    --panel-light: #a08a62;
    --cream: #f6ecc4;
    --cream-deep: #ecdca6;
    --band: #6b4f36;
    --band-dark: #553c28;
    --card: #94805a;
    --card-head: #745a3e;
    --card-foot: #6a4d34;
    --card-rule: #3f2a19;
    --text-light: #f7eccb;
    --text-soft: #c9b58d;
    --ornament: #7a6040;
    --logo: #7d6039;
  }
  * { box-sizing: border-box; margin: 0; padding: 0; }
  html, body { width: 1200px; height: 729px; overflow: hidden; }
  body {
    position: relative;
    background: radial-gradient(ellipse at 50% 30%, var(--bg-mid), var(--bg-dark) 70%);
    font-family: "Arimo", Arial, sans-serif;
  }
  .side-flourish {
    position: absolute; top: 30px; width: 100px; height: 620px;
    background: linear-gradient(180deg, rgba(170,140,100,.25), rgba(170,140,100,.08) 60%, rgba(190,160,115,.35));
    border-radius: 60px;
  }
  .side-flourish.left { left: 115px; }
  .side-flourish.right { left: 985px; }
  .page {
    position: absolute; left: 189px; top: 19px; width: 840px; height: 632px;
    background: linear-gradient(180deg, var(--panel-light) 0%, var(--panel) 40%, var(--panel) 100%);
    border: 1px solid #b39c6e; border-radius: 10px 10px 0 0;
    box-shadow: 0 0 14px rgba(0,0,0,.35);
  }
  .masthead {
    position: absolute; left: 4px; top: 4px; right: 4px; height: 112px;
    background: radial-gradient(ellipse at 50% 40%, #fbf3d2, var(--cream) 50%, var(--cream-deep));
    border-radius: 8px 8px 0 0;
  }
  .brand {
    position: absolute; left: 58px; top: 44px; display: flex; align-items: center; gap: 6px;
    font-family: "Libre Baskerville", Georgia, serif; font-size: 26px; color: var(--logo);
  }
  .brand .dot { width: 14px; height: 14px; border-radius: 50%; background: var(--logo); }
  .main-nav {
    position: absolute; left: 179px; top: 135px; width: 860px; height: 32px;
    background: linear-gradient(180deg, var(--band), var(--band-dark));
    border-top: 1px solid #8b6e4e; border-bottom: 1px solid #3a2617;
    box-shadow: 0 2px 5px rgba(0,0,0,.3);
    display: flex; align-items: center; padding-left: 40px;
  }
  .main-nav a {
    font-family: "Petit Formal Script", cursive; font-size: 11px; color: var(--text-light);
    text-decoration: none; margin-right: 22px; padding: 3px 6px;
  }
  .main-nav a.current { background: rgba(255,240,200,.15); border-radius: 3px; }
  .phone {
    position: absolute; right: 42px; top: 7px; display: flex; align-items: center; gap: 6px;
    font-family: "Petit Formal Script", cursive; font-size: 11px; color: var(--text-light);
  }
  .divider { position: absolute; left: 218px; width: 785px; height: 40px; }
  .divider.top { top: 205px; }
  .divider.bottom { top: 613px; height: 30px; }
  .section-title {
    position: absolute; left: 270px; top: 262px;
    font-family: "Libre Baskerville", Georgia, serif; font-size: 18px; color: var(--text-light);
    font-weight: normal;
  }
  .package {
    position: absolute; top: 293px; width: 242px; height: 288px;
    background: var(--card); border: 1px solid #5c442d; border-radius: 4px; overflow: hidden;
  }
  .package-head {
    height: 31px; background: linear-gradient(90deg, var(--card-head), #8c7052 60%, var(--card-head));
    font-family: "Libre Baskerville", Georgia, serif; font-size: 14px; color: var(--text-light);
    padding: 9px 0 0 22px; font-weight: normal;
  }
  .features { list-style: none; margin: 16px 0 0 14px; width: 208px; }
  .features li {
    display: flex; align-items: center; gap: 6px; height: 21.5px;
    font-size: 11.5px; color: var(--text-light);
    border-bottom: 1px dashed #b9a57d;
  }
  .package-price {
    position: absolute; left: 0; bottom: 0; width: 100%; height: 69px;
    background: var(--card-foot); border-top: 4px solid var(--card-rule);
  }
  .price-label { position: absolute; left: 26px; top: 5px; font-size: 11px; color: var(--text-soft); }
  .price-value { position: absolute; left: 43px; top: 18px; font-size: 38px; color: var(--text-light); line-height: 1; }
  .price-value sup { font-size: 20px; vertical-align: 16px; }
  .site-footer {
    position: absolute; left: 0; top: 651px; width: 1200px; height: 78px;
    background: var(--footer); border-top: 10px solid var(--footer-edge);
  }
  .footer-brand {
    position: absolute; left: 205px; top: 35px; display: flex; align-items: center; gap: 12px;
    font-family: "Libre Baskerville", Georgia, serif; font-size: 10px; color: var(--text-light);
  }
  .footer-brand .name { font-size: 13px; color: #c7b38b; }
  .social { position: absolute; left: 903px; top: 23px; display: flex; gap: 6px; }
  .social span {
    width: 32px; height: 32px; border-radius: 4px;
    background: linear-gradient(180deg, #b8a27a, #8f7a55); border: 1px solid #5e4a30;
  }
</style>
</head>
<body>
  <div class="side-flourish left" role="img" aria-label="Decorative floral scroll beside the page"></div>
  <div class="side-flourish right" role="img" aria-label="Decorative floral scroll beside the page"></div>

  <div class="page">
    <header class="masthead">
      <div class="brand"><span class="dot"></span>Veridel</div>
    </header>
  </div>

  <nav class="main-nav">
    <a href="#">About Us</a>
    <a href="#">VIP Club</a>
    <a href="#">Services</a>
    <a href="#">Package and Prices</a>
    <a href="#" class="current">Registration</a>
    <a href="#">Contact</a>
    <span class="phone">
      <svg width="12" height="14" viewBox="0 0 12 14"><path d="M2 1 L5 1 L6 4 L4 5 Q5 8 7 10 L8 8 L11 9 L11 12 Q10 13 8 13 Q1 10 1 3 Q1 1 2 1Z" fill="#f7eccb"/></svg>
      555-010-010
    </span>
  </nav>

  <svg class="divider top" viewBox="0 0 785 40" role="img" aria-label="Ornamental divider with central flourish">
    <line x1="10" y1="21" x2="775" y2="21" stroke="#6a5035" stroke-width="3"/>
    <ellipse cx="392" cy="21" rx="105" ry="18" fill="#7a6040" opacity=".8"/>
  </svg>

  <h2 class="section-title">Services</h2>

  <section class="package" style="left:245px">
    <h3 class="package-head">Package I</h3>
    <ul class="features">
      <li><svg width="20" height="10" viewBox="0 0 20 10"><path d="M0 5 H14 M9 1 L16 5 L9 9" stroke="#6a4d34" stroke-width="2" fill="none"/></svg>Nunc ac tortor sed lorem.</li>
      <li><svg width="20" height="10" viewBox="0 0 20 10"><path d="M0 5 H14 M9 1 L16 5 L9 9" stroke="#6a4d34" stroke-width="2" fill="none"/></svg>Nullam id ligula viverra nisi.</li>
      <li><svg width="20" height="10" viewBox="0 0 20 10"><path d="M0 5 H14 M9 1 L16 5 L9 9" stroke="#6a4d34" stroke-width="2" fill="none"/></svg>Aenean vel mauris eu.</li>
      <li><svg width="20" height="10" viewBox="0 0 20 10"><path d="M0 5 H14 M9 1 L16 5 L9 9" stroke="#6a4d34" stroke-width="2" fill="none"/></svg>Vivamus tempor augue.</li>
      <li><svg width="20" height="10" viewBox="0 0 20 10"><path d="M0 5 H14 M9 1 L16 5 L9 9" stroke="#6a4d34" stroke-width="2" fill="none"/></svg>Maecenas malesuada enim.</li>
    </ul>
    <div class="package-price"><span class="price-label">Price</span><span class="price-value">$580.<sup>95</sup></span></div>
  </section>

  <section class="package" style="left:490px">
    <h3 class="package-head">Package II</h3>
    <ul class="features">
      <li><svg width="20" height="10" viewBox="0 0 20 10"><path d="M0 5 H14 M9 1 L16 5 L9 9" stroke="#6a4d34" stroke-width="2" fill="none"/></svg>Nunc ac tortor sed lorem.</li>
      <li><svg width="20" height="10" viewBox="0 0 20 10"><path d="M0 5 H14 M9 1 L16 5 L9 9" stroke="#6a4d34" stroke-width="2" fill="none"/></svg>Nullam id ligula viverra nisi.</li>
      <li><svg width="20" height="10" viewBox="0 0 20 10"><path d="M0 5 H14 M9 1 L16 5 L9 9" stroke="#6a4d34" stroke-width="2" fill="none"/></svg>Aenean vel mauris eu.</li>
      <li><svg width="20" height="10" viewBox="0 0 20 10"><path d="M0 5 H14 M9 1 L16 5 L9 9" stroke="#6a4d34" stroke-width="2" fill="none"/></svg>Vivamus tempor augue.</li>
      <li><svg width="20" height="10" viewBox="0 0 20 10"><path d="M0 5 H14 M9 1 L16 5 L9 9" stroke="#6a4d34" stroke-width="2" fill="none"/></svg>Maecenas malesuada enim.</li>
    </ul>
    <div class="package-price"><span class="price-label">Price</span><span class="price-value">$740.<sup>95</sup></span></div>
  </section>

  <section class="package" style="left:734px">
    <h3 class="package-head">Package III</h3>
    <ul class="features">
      <li><svg width="20" height="10" viewBox="0 0 20 10"><path d="M0 5 H14 M9 1 L16 5 L9 9" stroke="#6a4d34" stroke-width="2" fill="none"/></svg>Nunc ac tortor sed lorem.</li>
      <li><svg width="20" height="10" viewBox="0 0 20 10"><path d="M0 5 H14 M9 1 L16 5 L9 9" stroke="#6a4d34" stroke-width="2" fill="none"/></svg>Nullam id ligula viverra nisi.</li>
      <li><svg width="20" height="10" viewBox="0 0 20 10"><path d="M0 5 H14 M9 1 L16 5 L9 9" stroke="#6a4d34" stroke-width="2" fill="none"/></svg>Aenean vel mauris eu.</li>
      <li><svg width="20" height="10" viewBox="0 0 20 10"><path d="M0 5 H14 M9 1 L16 5 L9 9" stroke="#6a4d34" stroke-width="2" fill="none"/></svg>Vivamus tempor augue.</li>
      <li><svg width="20" height="10" viewBox="0 0 20 10"><path d="M0 5 H14 M9 1 L16 5 L9 9" stroke="#6a4d34" stroke-width="2" fill="none"/></svg>Maecenas malesuada enim.</li>
    </ul>
    <div class="package-price"><span class="price-label">Price</span><span class="price-value">$990.<sup>95</sup></span></div>
  </section>

  <svg class="divider bottom" viewBox="0 0 785 30" role="img" aria-label="Ornamental divider with small central flourish">
    <line x1="10" y1="15" x2="775" y2="15" stroke="#6a5035" stroke-width="2"/>
    <ellipse cx="387" cy="15" rx="32" ry="11" fill="#7a6040" opacity=".8"/>
  </svg>

  <footer class="site-footer">
    <div class="footer-brand"><span class="name">Veridel</span><span>© Veridel 2010. All rights reserved.</span></div>
    <div class="social"><span></span><span></span><span></span></div>
  </footer>
</body>
</html>
```